Floral Design for Weddings And Events

I create floral designs for weddings and events. I create unusual designs that people will remember.

Industry/Entity Type

Floral

Contact Information for Business Card

Petals
Weddings and Events
Marlene Hayward, owner/designer
3718 Delwood Ct
Fernhill, CA 93105
marlenehaywardq@mailvista.net
707 555-0172

Requirements
Must have
• I would like the name of the business, PETALS, to Stand Out!! I like clean, bold lines.. nothing foo-foo! Must be easy to read I'm looking for a design that catches your eye and represents my creativity. I want my card to show the potential customer that I'm unique and creative
Nice to have
• I'm thinking of the name PETALS maybe worked into the design... I'm open to your creative ideas!!!! The name must be very legible
Should not have
• I'm open to any colors other that pink and yellow..nothing Foo-Foo or flowery..

```html
<!DOCTYPE html>
<html lang="en">
<head>
<meta charset="utf-8">
<title>Petals — Business Card</title>
<link rel="stylesheet" href="https://fonts.googleapis.com/css2?family=Arimo:wght@400&display=swap">
<style>
  :root {
    --card-bg: #202020;
    --ink-light: #f4f4f4;
    --accent: #e0542b;
  }
  html, body {
    margin: 0;
    padding: 0;
    width: 1200px;
    height: 728px;
    overflow: hidden;
    background: var(--card-bg);
  }
  .business-card {
    position: relative;
    width: 1200px;
    height: 728px;
    background: var(--card-bg);
    font-family: "Arimo", "Helvetica Neue", Arial, sans-serif;
    color: var(--ink-light);
  }
  .business-card p { margin: 0; line-height: 1; position: absolute; white-space: nowrap; }

  .brand-name {
    left: 88px;
    top: 78px;
    font-size: 86px;
    letter-spacing: 1px;
    font-weight: 400;
  }
  .brand-tagline {
    left: 88px;
    top: 180px;
    font-size: 27px;
    color: var(--accent);
  }
  .brand-rule {
    position: absolute;
    left: 386px;
    top: 195px;
    width: 703px;
    height: 2px;
    background: var(--accent);
  }

  .contact-block { text-align: right; right: 112px; }
  .person-name { font-size: 42px; top: 295px; }
  .person-role { font-size: 23px; top: 359px; color: var(--accent); }
  .contact-line { font-size: 28px; }
  .contact-address { top: 479px; }
  .contact-email { top: 526px; }
  .contact-phone { top: 573px; }
</style>
</head>
<body>
  <main class="business-card">
    <p class="brand-name">PETALS</p>
    <p class="brand-tagline">Weddings and Events</p>
    <div class="brand-rule"></div>

    <p class="contact-block person-name">Marlene Hayward</p>
    <p class="contact-block person-role">owner/designer</p>

    <p class="contact-block contact-line contact-address">3718 Delwood Ct Fernhill, CA 93105</p>
    <p class="contact-block contact-line contact-email">marlenehaywardq@mailvista.net</p>
    <p class="contact-block contact-line contact-phone">707 555-0172</p>
  </main>
</body>
</html>
```